Commercial Office Fitout company needs a simple website

We need a website for our company Harbourline Fitouts (QLD) Pty Ltd. We are in the construction industry and we specialise in commercial office fitouts (partitions/glass/doors). Our company colours are black and silver. Please use our logo attached.
We only need an "about us" section, a "portfolio" section where we display some pictures of our work, and a "contact us" section. We would like our website to be simple, effective, professional and modern.

Industry/Entity Type

Construction

Number of Pages Required

1 page

```html
<!DOCTYPE html>
<html lang="en">
<head>
<meta charset="utf-8">
<title>Harbourline Fitouts (QLD) Pty Ltd</title>
<link rel="stylesheet" href="https://fonts.googleapis.com/css2?family=Roboto+Condensed:wght@300;400;700&family=Lato:wght@400;700&display=swap">
<style>
:root{
  --ink:#111111;
  --ink-soft:#1c1c1c;
  --grey:#7a7a7a;
  --grey-light:#9a9a9a;
  --silver:#c9cbcd;
  --panel:#f0f0f0;
  --field:#f2f2f2;
  --field-line:#cfcfcf;
  --white:#ffffff;
  --head:"Roboto Condensed", Arial, sans-serif;
  --body:"Lato", Arial, sans-serif;
}
*{box-sizing:border-box;margin:0;padding:0}
html,body{width:1200px;height:2817px;overflow:hidden;background:var(--white)}
body{position:relative;font-family:var(--body);color:var(--ink)}
.abs{position:absolute}
.section{position:absolute;left:0;width:1200px}

/* Header */
.site-header{top:0;height:126px;background:var(--white)}
.brand{left:72px;top:30px;display:flex;align-items:center;gap:14px}
.brand-mark{width:46px;height:46px;background:var(--ink)}
.brand-name{font-family:var(--head);font-weight:700;font-size:21px;line-height:24px;color:var(--ink);letter-spacing:.5px;text-transform:uppercase}
.main-nav{right:79px;top:35px;display:flex;gap:0}
.main-nav a{font-family:var(--head);font-size:20px;color:#555;text-decoration:none;padding:0 24px;line-height:52px;height:52px;text-transform:uppercase}
.main-nav a.active{background:var(--ink);color:var(--white)}

/* Hero */
.hero{top:126px;height:520px;background:linear-gradient(100deg,#e9ecef 0%,#d7dadc 30%,#b9bcbf 55%,#e4e6e7 75%,#d8b23a 88%,#ece9df 100%)}
.hero-floor{left:0;bottom:0;width:1200px;height:210px;background:linear-gradient(180deg,rgba(120,120,120,.35),rgba(90,90,90,.55))}
.hero-caption{left:563px;top:285px;width:573px;height:152px;background:rgba(30,30,30,.78);color:var(--white);font-family:var(--head);font-size:36px;line-height:52px;text-align:right;padding:24px 44px 0 0;text-transform:uppercase}
.emblem{left:563px;top:605px;width:74px;height:74px;border-radius:50%;background:var(--white);border:6px solid var(--ink)}

/* Welcome */
.welcome{top:646px;height:321px;text-align:center}
.welcome h1{position:absolute;left:0;width:1200px;top:42px;font-family:var(--head);font-weight:400;font-size:46px;color:var(--ink);text-transform:uppercase}
.welcome h1 span{color:var(--grey)}
.welcome p{position:absolute;left:180px;width:840px;top:112px;font-size:15px;line-height:25px;color:var(--grey-light)}
.btn{position:absolute;font-family:var(--head);font-size:20px;text-transform:uppercase;display:flex;align-items:center;justify-content:center;text-decoration:none}
.btn-outline{border:2px solid var(--ink);color:var(--ink);background:var(--white)}
.btn-solid{background:var(--ink);color:var(--white)}

/* Services */
.services{top:967px;height:466px;background:linear-gradient(180deg,#2a2c2e 0%,#3a3d40 40%,#2c2e30 100%);color:var(--white);text-align:center}
.services h2{position:absolute;left:0;width:1200px;top:52px;font-family:var(--head);font-weight:400;font-size:44px;text-transform:uppercase}
.service{position:absolute;top:137px;width:320px}
.service svg{display:block;margin:0 auto}
.service h3{font-family:var(--head);font-weight:400;font-size:25px;margin-top:14px}
.service p{font-size:15px;line-height:25px;margin-top:6px;color:#f0f0f0}

/* Work */
.work{top:1433px;height:409px;background:var(--panel);text-align:center}
.work h2{position:absolute;left:0;width:1200px;top:50px;font-family:var(--head);font-weight:400;font-size:46px;text-transform:uppercase}
.work h2 span{color:var(--grey)}
.work-item{position:absolute;top:122px;width:235px;height:141px}

/* Call band */
.call{top:1842px;height:250px;background:linear-gradient(180deg,#25282b,#3b3f43 60%,#2a2d30);color:var(--white)}
.call-line{left:0;width:1200px;top:52px;display:flex;justify-content:center;align-items:center;gap:18px;font-family:var(--head);font-size:35px;text-transform:uppercase}
.call-number{font-size:35px}

/* Clients & quote */
.lower{top:2092px;height:505px}
.lower h2{position:absolute;top:58px;font-family:var(--head);font-weight:400;font-size:46px;text-transform:uppercase}
.lower h2 span{color:var(--grey)}
.avatar{position:absolute;left:79px;width:124px;height:124px;border-radius:50%;background:linear-gradient(160deg,#c9bfb6,#8a7a6c);border:3px solid #e3e3e3}
.testimonial{position:absolute;left:231px;width:312px;font-size:15px;line-height:25px;color:var(--grey-light)}
.testimonial cite{display:block;font-style:normal;color:var(--ink);font-size:14px;margin-top:4px;text-transform:uppercase}
.field{position:absolute;background:var(--field);border:1px solid var(--field-line);font-size:14px;color:#777;padding:10px 10px}

/* Footer */
.site-footer{top:2597px;height:220px;background:var(--ink);color:var(--white)}
.footer-nav{left:79px;top:26px;display:flex;gap:44px;font-size:17px}
.footer-nav a{color:#9a9a9a;text-decoration:none}
.footer-nav a.active{color:var(--white)}
.social{right:79px;top:28px;display:flex;gap:18px}
.social span{width:20px;height:20px;background:#bdbdbd;border-radius:3px}
.footer-rule{left:79px;top:70px;width:1042px;height:1px;background:#333}
.footer-title{left:79px;top:96px;font-size:17px}
.contact-item{position:absolute;top:128px;display:flex;align-items:center;gap:16px;font-size:14px;line-height:23px;color:#bbb}
.contact-item .ic{width:52px;height:52px;border-radius:50%;background:var(--white);flex:none;display:flex;align-items:center;justify-content:center}
.contact-item strong{color:var(--white);font-weight:700}
.copyright{left:891px;top:132px;font-size:14px;line-height:25px;color:#bbb}
.copyright b{color:var(--white);font-weight:400}
</style>
</head>
<body>

<header class="section site-header">
  <div class="abs brand">
    <div class="brand-mark"></div>
    <div class="brand-name">Harbourline Fitouts<br>(QLD) Pty Ltd</div>
  </div>
  <nav class="abs main-nav">
    <a class="active" href="#">Home</a>
    <a href="#">About</a>
    <a href="#">Services</a>
    <a href="#">Portfolio</a>
    <a href="#">Contact</a>
  </nav>
</header>

<section class="section hero" role="img" aria-label="Photo of a bright modern office reception with a curved glass desk and green chairs">
  <div class="abs hero-floor"></div>
  <div class="abs hero-caption">Lorem ipsum is simply<br>dummy text and printing</div>
</section>

<section class="section welcome">
  <h1><span>Welcome to</span> Harbourline Fitouts</h1>
  <p>Lorem Ipsum is simply dummy text of the printing and typesetting industry. Lorem Ipsum has been the industry's standard dummy text ever since the 1500s, when an unknown printer took a galley of type and scrambled it to make a type specimen book.</p>
  <a class="btn btn-outline" href="#" style="left:437px;top:210px;width:147px;height:51px">Read More</a>
  <a class="btn btn-solid" href="#" style="left:605px;top:210px;width:156px;height:51px">Contact Us</a>
</section>
<div class="abs emblem"></div>

<section class="section services" aria-label="Services">
  <h2>Services We Provide</h2>
  <div class="service" style="left:73px">
    <svg width="130" height="150" viewBox="0 0 130 150"><polygon points="65,3 127,39 127,111 65,147 3,111 3,39" fill="none" stroke="#fff" stroke-width="2"/><g fill="#fff"><rect x="40" y="62" width="34" height="22"/><rect x="54" y="84" width="6" height="8"/><rect x="34" y="94" width="62" height="5"/><rect x="38" y="99" width="4" height="14"/><rect x="88" y="99" width="4" height="14"/></g></svg>
    <h3>Office Partitions</h3>
    <p>Lorem Ipsum is simply dummy text of the printing and typesetting industry. Lorem Ipsum has been the industry.</p>
  </div>
  <div class="service" style="left:441px">
    <svg width="130" height="150" viewBox="0 0 130 150"><polygon points="65,3 127,39 127,111 65,147 3,111 3,39" fill="#fff"/><g fill="#111"><rect x="40" y="50" width="26" height="56"/><rect x="66" y="64" width="26" height="42"/><rect x="36" y="106" width="60" height="4"/></g><g fill="#fff"><rect x="45" y="56" width="5" height="5"/><rect x="56" y="56" width="5" height="5"/><rect x="45" y="67" width="5" height="5"/><rect x="56" y="67" width="5" height="5"/><rect x="45" y="78" width="5" height="5"/><rect x="56" y="78" width="5" height="5"/><rect x="71" y="70" width="5" height="5"/><rect x="82" y="70" width="5" height="5"/><rect x="71" y="81" width="5" height="5"/><rect x="82" y="81" width="5" height="5"/><rect x="50" y="92" width="6" height="14"/></g></svg>
    <h3>Office Glasses</h3>
    <p>Lorem Ipsum is simply dummy text of the printing and typesetting industry. Lorem Ipsum has been the industry.</p>
  </div>
  <div class="service" style="left:809px">
    <svg width="130" height="150" viewBox="0 0 130 150"><polygon points="65,3 127,39 127,111 65,147 3,111 3,39" fill="none" stroke="#fff" stroke-width="2"/><rect x="46" y="46" width="38" height="60" fill="none" stroke="#fff" stroke-width="3"/><polygon points="50,48 70,54 70,110 50,104" fill="#fff"/><circle cx="65" cy="80" r="2" fill="#111"/></svg>
    <h3>Office Doors</h3>
    <p>Lorem Ipsum is simply dummy text of the printing and typesetting industry. Lorem Ipsum has been the industry.</p>
  </div>
</section>

<section class="section work" aria-label="Our work">
  <h2><span>Our</span> Work</h2>
  <div class="work-item" style="left:77px;background:linear-gradient(180deg,#e6e8ea,#b9bbbd)" role="img" aria-label="Photo of an office corridor with workstations"></div>
  <div class="work-item" style="left:347px;background:linear-gradient(160deg,#d8ecf8,#3d8ac4 55%,#1d4f82)" role="img" aria-label="Photo of glass office towers against blue sky"></div>
  <div class="work-item" style="left:618px;background:linear-gradient(180deg,#f4f5f6,#c9cbcd)" role="img" aria-label="Photo of an open plan office with white desks"></div>
  <div class="work-item" style="left:888px;background:linear-gradient(180deg,#e9eef0,#9fb08a 60%,#8fae3a)" role="img" aria-label="Photo of a breakout area with green chairs"></div>
  <a class="btn btn-outline" href="#" style="left:528px;top:297px;width:144px;height:49px">View All</a>
</section>

<section class="section call" role="img" aria-label="Dark photo of city office buildings behind a call to action">
  <div class="abs call-line">
    <span>If you work with us, call us now</span>
    <svg width="62" height="62" viewBox="0 0 62 62"><circle cx="31" cy="31" r="29" fill="none" stroke="#fff" stroke-width="2"/><path d="M22 18c2-1 4 0 5 2l2 5c1 2 0 3-1 4l-2 2c2 4 5 7 9 9l2-2c1-1 2-2 4-1l5 2c2 1 3 3 2 5l-1 3c-1 2-3 2-5 2-12-2-21-11-23-23 0-2 0-4 2-5z" fill="#fff"/></svg>
    <span class="call-number">07 3555 0142</span>
  </div>
  <a class="btn" href="#" style="left:496px;top:128px;width:208px;height:56px;background:#fff;color:#111;font-size:19px">Contact Us Now</a>
</section>

<section class="section lower">
  <h2 style="left:79px"><span>What our</span> client say</h2>
  <div class="avatar" style="top:139px" role="img" aria-label="Client portrait photo"></div>
  <p class="testimonial" style="top:142px">Lorem Ipsum is simply dummy text of the printing and typesetting industry. Lorem Ipsum has been the industry.<cite>- Client Name</cite></p>
  <div class="avatar" style="top:284px" role="img" aria-label="Client portrait photo"></div>
  <p class="testimonial" style="top:288px;left:236px">Lorem Ipsum is simply dummy text of the printing and typesetting industry. Lorem Ipsum has been the industry.<cite>- Client Name</cite></p>

  <h2 style="left:637px"><span>Get a</span> free quote</h2>
  <div class="field" style="left:640px;top:130px;width:230px;height:40px">Enter Name</div>
  <div class="field" style="left:890px;top:130px;width:229px;height:40px">Enter Contact No.</div>
  <div class="field" style="left:640px;top:192px;width:479px;height:40px">Enter Email Id</div>
  <div class="field" style="left:640px;top:254px;width:479px;height:112px">Enter Message</div>
  <a class="btn btn-solid" href="#" style="left:642px;top:389px;width:132px;height:45px;font-size:18px">Submit</a>
</section>

<footer class="section site-footer">
  <nav class="abs footer-nav">
    <a class="active" href="#">Home</a>
    <a href="#">About</a>
    <a href="#">Services</a>
    <a href="#">Portfolio</a>
    <a href="#">Contact</a>
  </nav>
  <div class="abs social" aria-label="Social links"><span></span><span></span><span></span></div>
  <div class="abs footer-rule"></div>
  <div class="abs footer-title">Contact Us</div>
  <div class="contact-item" style="left:75px">
    <span class="ic"><svg width="20" height="26" viewBox="0 0 20 26"><path d="M10 0C4.5 0 0 4.3 0 9.7 0 17 10 26 10 26s10-9 10-16.3C20 4.3 15.5 0 10 0zm0 13.5a4 4 0 110-8 4 4 0 010 8z" fill="#111"/></svg></span>
    <span>Lorem Ipsum is dummy<br>text of the printing.</span>
  </div>
  <div class="contact-item" style="left:347px">
    <span class="ic"><svg width="22" height="22" viewBox="0 0 22 22"><path d="M4 1c1.5-.6 2.6 0 3.2 1.3l1.4 3.3c.5 1.3 0 2-.8 2.8l-1.3 1.2c1.3 2.7 3.3 4.7 6 6l1.2-1.3c.8-.8 1.6-1.3 2.8-.8l3.3 1.4c1.3.6 1.9 1.7 1.3 3.2l-.6 1.5c-.6 1.3-2 1.6-3.3 1.4C9.6 20 2 12.4.9 4.8.7 3.5 1 2 2.4 1.6z" fill="#111"/></svg></span>
    <strong>07 3555 0142</strong>
  </div>
  <div class="contact-item" style="left:618px">
    <span class="ic"><svg width="22" height="16" viewBox="0 0 22 16"><rect x="1" y="1" width="20" height="14" rx="2" fill="none" stroke="#111" stroke-width="2"/><path d="M2 2l9 7 9-7" fill="none" stroke="#111" stroke-width="2"/></svg></span>
    <span>info@harbourlinefitouts.com</span>
  </div>
  <div class="abs copyright">© <b>HARBOURLINE FITOUTS</b> - 2016.<br>All Rights Reserved.</div>
</footer>

</body>
</html>
```